Electrical company needs professional eye catching business cards

I am an electrician who needs business cards. I have attached two images which you can use. The file ab.jpg I would atleast like to be used. The file named back.jpg can be used on the back or not... up to you.

The information on my business cards I will have displayed will be-
My name
Mobile number
web site url
Licence number
ABN

Also as another request, I would like the word "Electrician" on the front of the card somewhere. Maybe under my name or something?

Industry/Entity Type

Electrician

```html
<!DOCTYPE html>
<html lang="en">
<head>
<meta charset="utf-8">
<title>Voltwise Installations – Business Card</title>
<link rel="stylesheet" href="https://fonts.googleapis.com/css2?family=Open+Sans:wght@400;600;700&display=swap">
<style>
  :root {
    --backdrop: #d6d6d4;
    --brand-blue: #22399a;
    --deep-blue: #1f3a8f;
    --slate: #2f4660;
    --ink: #34465e;
    --muted: #5d5d5d;
    --paper: #f7f7f5;
    --pill: #e9ecf2;
  }
  * { box-sizing: border-box; margin: 0; padding: 0; }
  html, body {
    width: 1200px; height: 1112px; overflow: hidden;
    background: var(--backdrop);
    font-family: "Open Sans", Arial, sans-serif;
  }
  .card {
    position: absolute; left: 180px; width: 840px; height: 480px;
    overflow: hidden; box-shadow: 0 6px 18px rgba(0,0,0,.18);
  }
  /* Back face */
  .card-back { top: 56px; background: var(--deep-blue); }
  .card-back .brand {
    position: absolute; left: 0; right: 0; top: 140px;
    display: flex; align-items: center; justify-content: center; gap: 22px;
    color: #fff;
  }
  .card-back .brand-square { width: 70px; height: 70px; background: #fff; border-radius: 6px; }
  .card-back .brand-name { font-size: 60px; font-weight: 600; letter-spacing: -.5px; }
  .card-back .web-pill {
    position: absolute; left: 50%; top: 290px; transform: translateX(-50%);
    background: var(--pill); color: var(--deep-blue);
    font-size: 22px; font-weight: 700; padding: 8px 30px; border-radius: 6px;
  }
  /* Front face */
  .card-front { top: 576px; background: var(--paper); }
  .card-front .brand {
    position: absolute; left: 56px; top: 40px;
    display: flex; align-items: center; gap: 16px; color: var(--ink);
  }
  .card-front .brand-square { width: 66px; height: 66px; background: var(--brand-blue); border-radius: 4px; }
  .card-front .brand-name { font-size: 58px; font-weight: 600; letter-spacing: -.5px; }
  .rule-blue { position: absolute; left: 0; top: 138px; width: 560px; height: 4px; background: var(--brand-blue); }
  .rule-slate { position: absolute; left: 600px; top: 238px; width: 240px; height: 4px; background: var(--slate); }
  .registration {
    position: absolute; left: 56px; top: 200px;
    color: var(--muted); font-size: 22px; line-height: 1.35;
  }
  .contact { position: absolute; left: 612px; top: 256px; }
  .contact .person { font-size: 30px; font-weight: 600; color: #1e1e1e; line-height: 1.1; }
  .contact .role { font-size: 24px; color: var(--brand-blue); font-weight: 600; margin-top: 2px; }
  .contact .phone { display: flex; align-items: center; gap: 10px; margin-top: 14px; font-size: 22px; color: #1e1e1e; }
  .band { position: absolute; }
  .band-blue { left: 0; top: 356px; width: 600px; height: 42px; background: var(--brand-blue); }
  .band-slate { left: 400px; top: 398px; width: 440px; height: 46px; background: var(--slate); }
  .web {
    position: absolute; left: 270px; top: 362px;
    display: flex; align-items: center; gap: 10px;
    color: #fff; font-size: 26px;
  }
</style>
</head>
<body>

<section class="card card-back" aria-label="Card back">
  <div class="brand">
    <span class="brand-square"></span>
    <span class="brand-name">Voltwise Installations</span>
  </div>
  <div class="web-pill">Website Url</div>
</section>

<section class="card card-front" aria-label="Card front">
  <div class="brand">
    <span class="brand-square"></span>
    <span class="brand-name">Voltwise Installations</span>
  </div>
  <div class="rule-blue"></div>
  <div class="rule-slate"></div>

  <div class="registration">
    <p>Licence number</p>
    <p>ABN</p>
  </div>

  <div class="contact">
    <p class="person">Name</p>
    <p class="role">Electrician</p>
    <p class="phone">
      <svg width="20" height="24" viewBox="0 0 20 24" aria-hidden="true">
        <path d="M5 1 L9 6 L6.5 9 C8 13 10 16 13 18 L16 15.5 L19.5 20 L16 23 C9 22 2 13 1.5 5 Z" fill="var(--brand-blue)"/>
      </svg>
      555 010 234
    </p>
  </div>

  <div class="band band-blue"></div>
  <div class="band band-slate"></div>
  <div class="web">
    <svg width="24" height="24" viewBox="0 0 24 24" aria-hidden="true" fill="none" stroke="#fff" stroke-width="1.6">
      <circle cx="12" cy="12" r="10"/>
      <ellipse cx="12" cy="12" rx="4.5" ry="10"/>
      <line x1="2" y1="12" x2="22" y2="12"/>
      <path d="M4 6.5 H20 M4 17.5 H20"/>
    </svg>
    <span>web site url</span>
  </div>
</section>

</body>
</html>
```